Tellvane Advertisement for EV chargers

Project Overview:
We are excited to launch a new Tellvane ad campaign to promote our top-notch service of Electric Vehicle (EV) Charger Installation. This campaign aims to reach environmentally conscious individuals, homeowners, businesses, and EV owners seeking professional and reliable EV charger installation solutions. The primary goal is to increase brand awareness and generate leads for our EV charger installation service.
Target Audience:
Our target audience includes environmentally conscious homeowners, property managers, commercial businesses, and individuals who own or plan to purchase an electric vehicle. The age range for our target audience is between 25 to 65 years old, residing in [your service area location] or nearby regions.
Key Message:
The advertisement should convey the following key messages:
"Power Up Your Ride with Professional EV Charger Installation."
"Fast and Reliable Service for Home and Business EV Charging Solutions."
"Go Green with Clean Energy and Eco-friendly EV Charging."
"Experienced Installers for Hassle-free EV Charger Setups."
Design Requirements:
Dimensions: The advertisement should comply with Tellvane's recommended ad dimensions (e.g., 1200 x 628 pixels).
Branding: Incorporate our company logo and colors (Logo attached).
Visuals: Use high-quality images or graphics showcasing electric vehicles being charged at home and in commercial settings, highlighting the ease and convenience of the process.
Call-to-Action (CTA): Include a clear and compelling CTA button, such as "Get a Quote," "Book Now," or "Learn More."
Text: Keep the text concise, using persuasive language to emphasize the benefits of our EV charger installation service, such as expert technicians, efficient installations, and cost savings.
Testimonials: Feature positive customer reviews or testimonials (if available) to build trust and credibility.
Coverage Area: Mention your service coverage area to ensure relevancy to the target audience.
Offer: If applicable, consider offering a limited-time discount or promotion for EV charger installation services.
Target Market(s)
Target Audience: Our target audience includes environmentally conscious homeowners, property managers, commercial businesses, and individuals who own or plan to purchase an electric vehicle. The age range for our target audience is between 25 to 65 years old, residing in [your service area location] or nearby regions.
Requirements
Must have
- The advertisement should convey the following key messages: "Power Up Your Ride with Professional EV Charger Installation." "Fast and Reliable Service for Home and Business EV Charging Solutions." "Go Green with Clean Energy and Eco-friendly EV Charging." "Experienced Installers for Hassle-free EV Charger Setups." Design Requirements: Dimensions: The advertisement should comply with Tellvane's recommended ad dimensions (e.g., 1200 x 628 pixels). Branding: Incorporate our company logo and colors (Logo attached). Visuals: Use high-quality images or graphics showcasing electric vehicles being charged at home and in commercial settings, highlighting the ease and convenience of the process. Call-to-Action (CTA): Include a clear and compelling CTA button, such as "Get a Quote," "Book Now," or "Learn More." Text: Keep the text concise, using persuasive language to emphasize the benefits of our EV charger installation service, such as expert technicians, efficient installations, and cost savings. Testimonials: Feature positive customer reviews or testimonials (if available) to build trust and credibility. Coverage Area: Mention your service coverage area to ensure relevancy to the target audience. Offer: If applicable, consider offering a limited-time discount or promotion for EV charger installation services.

```html
<!DOCTYPE html>
<html lang="en">
<head>
<meta charset="utf-8">
<title>Tellvane EV Charger Installation Banner</title>
<link rel="stylesheet" href="https://fonts.googleapis.com/css2?family=Poppins:wght@400;500;600;700;800&display=swap">
<style>
  :root {
    --red: #c8202f;
    --red-dark: #a8151f;
    --navy: #1d2a3c;
    --sky-top: #bfe3f5;
    --sky-low: #dff0f8;
    --horizon: #8a929a;
    --asphalt: #2a3038;
    --asphalt-dark: #171b21;
    --white: #ffffff;
    --ink: #2b2b2b;
    --page: #eef0f2;
  }
  * { box-sizing: border-box; margin: 0; padding: 0; }
  html, body { width: 1200px; height: 718px; overflow: hidden; }
  body {
    background: var(--page);
    font-family: "Poppins", sans-serif;
    display: flex;
    align-items: center;
    justify-content: center;
  }
  .banner {
    position: relative;
    width: 1200px;
    height: 628px;
    overflow: hidden;
    background: var(--white);
  }
  .backdrop {
    position: absolute;
    inset: 0 0 67px 0;
    background: linear-gradient(180deg, var(--sky-top) 0%, var(--sky-low) 62%, var(--horizon) 65%, var(--asphalt) 76%, var(--asphalt-dark) 100%);
  }
  .vehicle-photo {
    position: absolute;
    top: 0;
    right: 0;
    width: 470px;
    height: 561px;
    background: radial-gradient(ellipse at 65% 55%, #f4f6f8 0%, #d9dee3 40%, rgba(160,170,180,0.6) 70%, rgba(160,170,180,0) 100%);
  }
  .brand {
    position: absolute;
    left: 46px;
    top: 44px;
  }
  .brand-name {
    display: block;
    font-size: 60px;
    font-weight: 700;
    color: var(--red);
    line-height: 1;
    letter-spacing: 0.5px;
  }
  .brand-tagline {
    margin-top: 26px;
    font-size: 13px;
    font-weight: 400;
    color: var(--navy);
    letter-spacing: -0.2px;
  }
  .headline {
    position: absolute;
    left: 44px;
    top: 168px;
    font-size: 76px;
    font-weight: 800;
    color: var(--red);
    line-height: 1;
    letter-spacing: -1px;
  }
  .subhead {
    position: absolute;
    left: 45px;
    top: 244px;
    font-size: 42px;
    font-weight: 800;
    color: var(--navy);
    line-height: 47px;
    letter-spacing: -1px;
    white-space: nowrap;
  }
  .benefits {
    position: absolute;
    left: 45px;
    top: 384px;
    display: flex;
    list-style: none;
  }
  .benefit {
    display: flex;
    gap: 12px;
    font-size: 20px;
    font-weight: 600;
    color: var(--white);
    line-height: 25px;
  }
  .benefit:nth-child(1) { width: 210px; }
  .benefit:nth-child(2) { width: 234px; }
  .benefit svg { flex: none; }
  .pitch {
    position: absolute;
    left: 46px;
    top: 469px;
    font-size: 19px;
    font-weight: 400;
    color: var(--white);
    line-height: 24px;
  }
  .cta {
    position: absolute;
    left: 436px;
    top: 474px;
    width: 242px;
    height: 44px;
    border-radius: 22px;
    background: linear-gradient(180deg, var(--red) 0%, var(--red-dark) 100%);
    color: var(--white);
    font-size: 27px;
    font-weight: 600;
    display: flex;
    align-items: center;
    justify-content: center;
    text-decoration: none;
  }
  .contact-bar {
    position: absolute;
    left: 0;
    bottom: 0;
    width: 100%;
    height: 67px;
    background: var(--white);
    display: flex;
    align-items: center;
    padding-left: 41px;
  }
  .contact-item {
    display: flex;
    align-items: center;
    gap: 5px;
    font-size: 20px;
    color: var(--ink);
    white-space: nowrap;
  }
  .contact-phone { width: 195px; }
  .contact-email { width: 309px; }
  .contact-web { width: 334px; }
  .offer-note {
    font-size: 9.5px;
    line-height: 12px;
    color: var(--ink);
    width: 300px;
  }
</style>
</head>
<body>
  <section class="banner">
    <div class="backdrop" role="img" aria-label="Soft sky fading to a dark paved driveway"></div>
    <div class="vehicle-photo" role="img" aria-label="Photo of a white electric car plugged into a wall-mounted charging station"></div>

    <div class="brand">
      <span class="brand-name">Tellvane</span>
      <p class="brand-tagline">EV CHARGING AND ENERGY SOLUTIONS</p>
    </div>

    <h1 class="headline">POWER UP</h1>
    <h2 class="subhead">YOUR RIDE WITH PROFESSIONAL<br>EV CHARGER INSTALLATION.</h2>

    <ul class="benefits">
      <li class="benefit">
        <svg width="28" height="28" viewBox="0 0 28 28"><circle cx="13" cy="14" r="11.5" fill="none" stroke="#fff" stroke-width="2.5"/><path d="M8 13l5 5 11-13" fill="none" stroke="var(--red)" stroke-width="3.2" stroke-linecap="round" stroke-linejoin="round"/></svg>
        <span>EXPERT<br>TECHNICIANS</span>
      </li>
      <li class="benefit">
        <svg width="28" height="28" viewBox="0 0 28 28"><circle cx="13" cy="14" r="11.5" fill="none" stroke="#fff" stroke-width="2.5"/><path d="M8 13l5 5 11-13" fill="none" stroke="var(--red)" stroke-width="3.2" stroke-linecap="round" stroke-linejoin="round"/></svg>
        <span>EFFICIENT<br>INSTALLATIONS</span>
      </li>
      <li class="benefit">
        <svg width="28" height="28" viewBox="0 0 28 28"><circle cx="13" cy="14" r="11.5" fill="none" stroke="#fff" stroke-width="2.5"/><path d="M8 13l5 5 11-13" fill="none" stroke="var(--red)" stroke-width="3.2" stroke-linecap="round" stroke-linejoin="round"/></svg>
        <span>COST SAVINGS</span>
      </li>
    </ul>

    <p class="pitch">Experienced Installers for<br>Hassle-free EV Charger Setups.</p>
    <a class="cta" href="#">LEARN MORE</a>

    <footer class="contact-bar">
      <span class="contact-item contact-phone">
        <svg width="22" height="22" viewBox="0 0 22 22"><circle cx="11" cy="11" r="10" fill="var(--red)"/><path d="M7.5 6.5l2 2-1 1.5c.8 1.6 1.9 2.7 3.5 3.5l1.5-1 2 2-1.2 1.4c-3.5-.5-6.7-3.7-7.2-7.2z" fill="#fff"/></svg>
        (07) 3000 4812
      </span>
      <span class="contact-item contact-email">
        <svg width="22" height="22" viewBox="0 0 22 22"><circle cx="11" cy="11" r="10" fill="var(--red)"/><rect x="6" y="7.5" width="10" height="7" fill="none" stroke="#fff" stroke-width="1.3"/><path d="M6 7.5l5 4 5-4" fill="none" stroke="#fff" stroke-width="1.3"/></svg>
        info@tellvane.com.au
      </span>
      <span class="contact-item contact-web">
        <svg width="22" height="22" viewBox="0 0 22 22"><circle cx="11" cy="11" r="10" fill="var(--red)"/><circle cx="11" cy="11" r="5.5" fill="none" stroke="#fff" stroke-width="1.3"/><path d="M5.5 11h11M11 5.5c-2.5 3-2.5 8 0 11M11 5.5c2.5 3 2.5 8 0 11" fill="none" stroke="#fff" stroke-width="1.1"/></svg>
        www.tellvane.com.au
      </span>
      <p class="offer-note">Offer: If applicable, consider offering a limited-time discount or promotion for EV charger installation services.</p>
    </footer>
  </section>
</body>
</html>
```